We are a Yacht Charter Broker servicing VIP clients on booking sailing catamarans and motor yacht...

We are looking for a wildly creative website to attract high net worth clients to work with us in booking their dream yacht vacation. A site that you think is 5 years ahead of its time. Sexy, modern and unique. Our company name is BRELLAVON. Our colors are navy blue and silver.
BLUE:
RGBB 0/44/92
CMYC 100/86/36/31
SILVER:
RGB 152/163/173
CMYK 43/29/25/0

HEX 98a3ad

Target Market(s)

High net worth people in need of white glove brokerage serving in finding and booking their dream yacht for a vacation of a lifetime.

Coding

Coded - Design and coding required

Number of Pages Required

1 page

Requirements
Must have
• Mobile friendly.
• Wildly creative and different. A website that we would expect to see 5 years from now.
• Pictures of yachts and or people on yachts. Palm tree landscapes.
• pictures of high end food related to the VIP yacht experience.
Nice to have
• Anything you feel would sell the yacht charter experience.
Should not have
• Nothing comes to mind.

```html
<!DOCTYPE html>
<html lang="en">
<head>
<meta charset="utf-8">
<title>Brellavon — Yacht Charter Broker</title>
<link href="https://fonts.googleapis.com/css2?family=Lora:wght@400;500&family=Open+Sans:wght@400;600&display=swap" rel="stylesheet">
<style>
  :root {
    --navy: #002c5c;
    --silver: #98a3ad;
    --silver-dark: #8e969e;
    --white: #ffffff;
    --text: #5b5f66;
    --quote: #3a3f48;
    --gallery-bg: #ececec;
    --line: #2b4a75;
  }
  * { box-sizing: border-box; margin: 0; padding: 0; }
  html, body { width: 1200px; height: 3782px; overflow: hidden; }
  body { background: var(--white); font-family: "Open Sans", Arial, sans-serif; color: var(--text); position: relative; }
  h1, h2, h3 { font-weight: 400; }
  section, header, footer { position: absolute; left: 0; width: 1200px; overflow: hidden; }

  /* Hero */
  .hero { top: 0; height: 613px; }
  .hero-photo { position: absolute; inset: 0;
    background:
      linear-gradient(180deg, rgba(10,30,70,.45) 0, rgba(10,30,70,0) 70px),
      linear-gradient(180deg, rgba(0,0,0,0) 0%, rgba(0,0,0,0) 48%, rgba(16,98,176,.85) 72%, #0a4f98 100%),
      linear-gradient(100deg, #9ea89a 0%, #c9c6b4 25%, #d6d1c0 42%, #b7b9ae 58%, #86a6b8 76%, #90b6cf 100%);
  }
  .logo-disc { position: absolute; left: -190px; top: -470px; width: 670px; height: 600px; border-radius: 50%; background: var(--white); }
  .logo { position: absolute; left: 131px; top: 22px; width: 260px; text-align: center; color: var(--navy); }
  .logo-name { font-family: "Lora", Georgia, serif; font-size: 30px; letter-spacing: 5px; line-height: 1; }
  .logo-tag { font-family: "Lora", Georgia, serif; font-size: 8px; letter-spacing: 2.5px; margin-top: 6px; }
  .nav { position: absolute; top: 10px; left: 517px; display: flex; align-items: center; font-family: "Lora", Georgia, serif; font-size: 12px; color: var(--white); }
  .nav a { color: var(--white); text-decoration: none; margin-right: 28px; }
  .nav a.current { text-decoration: underline; }
  .nav .nav-book { border: 1px solid var(--white); padding: 4px 9px; margin: 0 0 0 -4px; }
  .hero-title { position: absolute; right: 134px; top: 168px; text-align: right; font-family: "Lora", Georgia, serif; font-size: 30px; line-height: 40px; color: var(--white); letter-spacing: .5px; }
  .hero-btn { position: absolute; left: 890px; top: 252px; width: 176px; height: 43px; border: 1px solid var(--white); color: var(--white); font-family: "Lora", Georgia, serif; font-size: 13px; display: flex; align-items: center; justify-content: center; }
  .arrow { position: absolute; width: 22px; height: 40px; }

  /* Section heading */
  .heading { position: absolute; left: 0; width: 1200px; text-align: center; font-family: "Lora", Georgia, serif; font-size: 33px; font-weight: 400; color: var(--navy); letter-spacing: .5px; line-height: 1.2; }
  .divider { position: absolute; left: 403px; width: 394px; height: 16px; }

  /* Welcome */
  .welcome { top: 613px; height: 340px; }
  .welcome-text { position: absolute; left: 166px; top: 173px; width: 896px; text-align: center; font-size: 12.5px; line-height: 22px; }

  /* Services */
  .services { top: 953px; height: 416px; background: linear-gradient(180deg, #8d98a4 0%, #9aa4ae 50%, #8f9aa5 100%); }
  .services-photo { position: absolute; inset: 0; background: radial-gradient(ellipse 520px 180px at 580px 170px, rgba(255,255,255,.22), rgba(255,255,255,0)); }
  .card { position: absolute; top: 181px; width: 217px; height: 154px; background: var(--white); text-align: center; }
  .card svg { position: absolute; left: 77px; top: 26px; }
  .card-label { position: absolute; left: 0; right: 0; top: 109px; font-family: "Lora", Georgia, serif; font-size: 14px; color: var(--navy); }

  /* Yachts */
  .yachts { top: 1369px; height: 648px; }
  .yacht-frame { position: absolute; left: 131px; top: 214px; width: 430px; height: 354px; background: #e6e7e9; }
  .yacht-photo { position: absolute; left: 146px; top: 189px; width: 429px; height: 363px; background: linear-gradient(180deg, #1f5fae 0%, #2c73bf 35%, #0f4b93 60%, #083b7b 100%); }
  .yacht-title { position: absolute; left: 625px; top: 230px; font-family: "Lora", Georgia, serif; font-size: 15px; font-weight: 400; color: var(--navy); }
  .yacht-text { position: absolute; left: 625px; top: 264px; width: 445px; font-size: 11.5px; line-height: 20.5px; }
  .btn-outline { position: absolute; border: 1px solid var(--navy); color: var(--navy); font-family: "Lora", Georgia, serif; font-size: 13px; display: flex; align-items: center; justify-content: center; }

  /* Gallery */
  .gallery { top: 2017px; height: 726px; background: var(--gallery-bg); }
  .tile { position: absolute; }

  /* Reviews */
  .reviews { top: 2743px; height: 408px; }
  .quote { position: absolute; left: 120px; top: 188px; width: 960px; text-align: center; font-family: "Lora", Georgia, serif; font-size: 15.5px; line-height: 26px; color: var(--quote); }
  .reviewer { position: absolute; left: 0; width: 1200px; top: 281px; text-align: center; font-family: "Lora", Georgia, serif; font-size: 15px; color: var(--navy); }
  .dots { position: absolute; left: 558px; top: 321px; display: flex; gap: 12px; }
  .dots span { width: 9px; height: 9px; border-radius: 50%; background: #d0d4d9; }
  .dots span.on { background: var(--navy); }

  /* Booking */
  .booking { top: 3151px; height: 525px; background: linear-gradient(180deg, #12295a 0%, #1d3f7a 45%, #2a5590 75%, #1c3a6e 100%); }
  .booking-glow { position: absolute; inset: 0; background: radial-gradient(ellipse 300px 260px at 1000px 440px, rgba(170,190,220,.35), rgba(0,0,0,0)), radial-gradient(ellipse 260px 300px at 120px 120px, rgba(5,15,40,.5), rgba(0,0,0,0)); }
  .field { position: absolute; background: var(--white); font-size: 11px; color: #666; padding: 9px 10px; }
  .btn-light { position: absolute; border: 1px solid var(--white); color: var(--white); font-family: "Lora", Georgia, serif; font-size: 13px; display: flex; align-items: center; justify-content: center; }

  /* Footer */
  .footer { top: 3676px; height: 106px; background: var(--silver-dark); color: var(--white); }
  .footer-links { position: absolute; left: 134px; top: 29px; font-size: 11px; display: flex; }
  .footer-links span { padding: 0 9px; border-left: 1px solid rgba(255,255,255,.7); line-height: 11px; }
  .footer-links span:first-child { padding-left: 0; border-left: 0; }
  .copyright { position: absolute; left: 134px; top: 63px; font-size: 10.5px; }
  .social { position: absolute; left: 940px; top: 44px; display: flex; gap: 18px; }
  .social span { width: 16px; height: 16px; border-radius: 50%; background: var(--white); }
</style>
</head>
<body>

<header class="hero">
  <div class="hero-photo" role="img" aria-label="White motor yacht cruising past tall limestone cliffs on deep blue sea"></div>
  <div class="logo-disc"></div>
  <div class="logo">
    <div class="logo-name">BRELLAVON</div>
    <div class="logo-tag">YACHT CHARTER BROKER</div>
  </div>
  <nav class="nav">
    <a class="current">HOME</a><a>ABOUT</a><a>YACHTS</a><a>SERVICES</a><a>GALLERY</a><a>CONTACT US</a><a class="nav-book">BOOK NOW</a>
  </nav>
  <div class="hero-title">CRAS AUGUE MAGNA<br>PLACERAT EGET NULLA</div>
  <div class="hero-btn">VIEW OUR SERVICES</div>
  <svg class="arrow" style="left:47px;top:290px" viewBox="0 0 22 40"><polyline points="16,6 4,20 16,34" fill="none" stroke="#fff" stroke-width="3"/></svg>
  <svg class="arrow" style="left:1131px;top:290px" viewBox="0 0 22 40"><polyline points="6,6 18,20 6,34" fill="none" stroke="#fff" stroke-width="3"/></svg>
</header>

<section class="welcome">
  <h1 class="heading" style="top:72px">WELCOME TO BRELLAVON</h1>
  <svg class="divider" style="top:131px" viewBox="0 0 394 16"><line x1="0" y1="8" x2="180" y2="8" stroke="#2b4a75"/><line x1="214" y1="8" x2="394" y2="8" stroke="#2b4a75"/><circle cx="197" cy="8" r="6" fill="#002c5c"/></svg>
  <p class="welcome-text">Maecenas vel tortor accumsan quam varius imperdiet vel eget elit. Aenean facilisis tincidunt lectus, id dictum nisi luctus eget. Vivamus efficitur ex condimentum, malesuada eros eget, feugiat nibh. Sed tellus ex, imperdiet eget gravida sit amet, volutpat eget turpis. In nec ultricies est. Etiam mattis augue vehicula odio posuere, sit amet tempus lectus luctus. Nulla facilisi. Etiam vel massa elementum, bibendum tellus venenatis, feugiat massa. Curabitur venenatis lacinia ornare.</p>
</section>

<section class="services">
  <div class="services-photo" role="img" aria-label="Faded view of a motor yacht deck under a silver sky"></div>
  <h2 class="heading" style="top:66px;color:#fff">OUR SERVICES</h2>
  <svg class="divider" style="top:128px" viewBox="0 0 394 16"><line x1="0" y1="8" x2="180" y2="8" stroke="#fff"/><line x1="214" y1="8" x2="394" y2="8" stroke="#fff"/><circle cx="197" cy="8" r="6" fill="#fff"/></svg>

  <div class="card" style="left:134px">
    <svg width="62" height="62" viewBox="0 0 62 62" fill="none" stroke="#002c5c" stroke-width="2"><circle cx="31" cy="31" r="29"/><line x1="31" y1="13" x2="31" y2="40"/><path d="M31 15 L42 36 L31 36 Z"/><path d="M29 19 L21 36 L29 36 Z"/><path d="M16 40 H46 L42 46 H20 Z"/></svg>
    <div class="card-label">YACHTS</div>
  </div>
  <div class="card" style="left:371px">
    <svg width="62" height="62" viewBox="0 0 62 62" fill="none" stroke="#002c5c" stroke-width="2"><circle cx="31" cy="31" r="29"/><circle cx="31" cy="31" r="11"/><circle cx="31" cy="31" r="3"/><line x1="31" y1="10" x2="31" y2="52"/><line x1="10" y1="31" x2="52" y2="31"/><line x1="16" y1="16" x2="46" y2="46"/><line x1="46" y1="16" x2="16" y2="46"/></svg>
    <div class="card-label">SAILING</div>
  </div>
  <div class="card" style="left:610px">
    <svg width="62" height="62" viewBox="0 0 62 62" fill="none" stroke="#002c5c" stroke-width="2"><circle cx="31" cy="31" r="29"/><line x1="31" y1="12" x2="31" y2="38"/><path d="M31 14 L43 36 H31"/><path d="M29 18 L20 36 H29"/><path d="M14 39 H48"/><path d="M16 39 L19 45 H27 L29 39"/><path d="M33 39 L35 45 H43 L46 39"/></svg>
    <div class="card-label">CATAMARANS</div>
  </div>
  <div class="card" style="left:850px">
    <svg width="62" height="62" viewBox="0 0 62 62" fill="none" stroke="#002c5c" stroke-width="2"><circle cx="31" cy="31" r="29"/><circle cx="31" cy="31" r="11"/><path d="M17 16 V26 M14 16 V24 Q14 27 17 27 Q20 27 20 24 V16 M17 27 V46"/><path d="M45 46 V16 Q40 20 40 30 H45"/></svg>
    <div class="card-label">FOOD PREPARATIONS</div>
  </div>
</section>

<section class="yachts">
  <h2 class="heading" style="top:72px">OUR YACHTS</h2>
  <svg class="divider" style="top:135px" viewBox="0 0 394 16"><line x1="0" y1="8" x2="180" y2="8" stroke="#2b4a75"/><line x1="214" y1="8" x2="394" y2="8" stroke="#2b4a75"/><circle cx="197" cy="8" r="6" fill="#002c5c"/></svg>
  <div class="yacht-frame"></div>
  <div class="yacht-photo" role="img" aria-label="Sleek white motor yacht speeding across open blue water"></div>
  <h3 class="yacht-title">CRAS AUGUE MAGNA PLACERAT</h3>
  <p class="yacht-text">Fusce sollicitudin lorem et luctus volutpat. Proin placerat dapibus gravida. In tristique tristique nulla eget hendrerit. Maecenas vel tortor accumsan quam varius imperdiet vel eget elit. Aenean facilisis tincidunt lectus, id dictum nisi luctus eget. Vivamus efficitur ex condimentum, malesuada eros eget, feugiat nibh. Sed tellus ex, imperdiet eget gravida sit amet, volutpat eget turpis. In nec ultricies est. Etiam mattis augue vehicula odio posuere, sit amet tempus lectus luctus. Nulla facilisi. Etiam vel massa elementum, bibendum tellus venenatis, feugiat massa. Curabitur venenatis lacinia ornare. Cras sollicitudin cursus dui eu placerat.</p>
  <div class="btn-outline" style="left:625px;top:466px;width:114px;height:43px">BOOK NOW</div>
</section>

<section class="gallery">
  <h2 class="heading" style="top:70px">GALLERY</h2>
  <svg class="divider" style="top:131px" viewBox="0 0 394 16"><line x1="0" y1="8" x2="180" y2="8" stroke="#2b4a75"/><line x1="214" y1="8" x2="394" y2="8" stroke="#2b4a75"/><circle cx="197" cy="8" r="6" fill="#002c5c"/></svg>
  <div class="tile" style="left:134px;top:186px;width:221px;height:232px;background:linear-gradient(180deg,#6f9fc9 0%,#d9c7a6 55%,#8a6a4c 100%)" role="img" aria-label="Couple relaxing on a yacht deck at sunset"></div>
  <div class="tile" style="left:368px;top:186px;width:227px;height:232px;background:linear-gradient(180deg,#4f88c0 0%,#86b5d8 50%,#e3e8ec 100%)" role="img" aria-label="Guest resting on the bow of a yacht over calm sea"></div>
  <div class="tile" style="left:608px;top:186px;width:458px;height:232px;background:linear-gradient(180deg,#8fb3d4 0%,#e9e5dc 40%,#c9a46e 75%,#6b4a33 100%)" role="img" aria-label="Breakfast table set with fruit and pastries on a yacht deck"></div>
  <div class="tile" style="left:134px;top:436px;width:458px;height:214px;background:linear-gradient(180deg,#e6c48e 0%,#b58a5c 45%,#4a3a2f 100%)" role="img" aria-label="Friends gathered on deck against the evening sun"></div>
  <div class="tile" style="left:608px;top:436px;width:221px;height:214px;background:linear-gradient(160deg,#0a6f9e 0%,#1a93b9 50%,#0b5a88 100%)" role="img" aria-label="Aerial view of a sailing yacht on turquoise water"></div>
  <div class="tile" style="left:842px;top:436px;width:224px;height:214px;background:linear-gradient(180deg,#c7c9cb 0%,#e8e8e6 50%,#9a9a96 100%)" role="img" aria-label="Guest in white standing at a yacht helm"></div>
  <svg class="arrow" style="left:52px;top:406px" viewBox="0 0 22 40"><polyline points="16,10 6,20 16,30" fill="none" stroke="#333" stroke-width="2.5"/></svg>
  <svg class="arrow" style="left:1126px;top:406px" viewBox="0 0 22 40"><polyline points="6,10 16,20 6,30" fill="none" stroke="#333" stroke-width="2.5"/></svg>
</section>

<section class="reviews">
  <h2 class="heading" style="top:76px">REVIEWS</h2>
  <svg class="divider" style="top:135px" viewBox="0 0 394 16"><line x1="0" y1="8" x2="180" y2="8" stroke="#2b4a75"/><line x1="214" y1="8" x2="394" y2="8" stroke="#2b4a75"/><circle cx="197" cy="8" r="6" fill="#002c5c"/></svg>
  <p class="quote">“ Vivamus lacus justo, ultrices nec erat in, euismod iaculis mauris. Vivamus eleifend vitae nulla vel malesuada. In ac malesuada<br>lacus, et consectetur ante. Fusce vitae lectus sit amet mi pulvinar maximus. Aenean placerat, nibh vel accumsan aliquet,<br>magna nibh accumsan nibh, ac tempus nunc ipsum ac tellus. ”</p>
  <div class="reviewer">Adrian Vale, City</div>
  <div class="dots"><span class="on"></span><span></span><span></span><span></span></div>
</section>

<section class="booking">
  <div class="booking-glow" role="img" aria-label="Palm tree silhouettes over a tropical shore at dusk, tinted navy"></div>
  <h2 class="heading" style="top:78px;color:#fff">BOOK NOW</h2>
  <svg class="divider" style="top:137px" viewBox="0 0 394 16"><line x1="0" y1="8" x2="180" y2="8" stroke="#fff"/><line x1="214" y1="8" x2="394" y2="8" stroke="#fff"/><circle cx="197" cy="8" r="6" fill="#fff"/></svg>
  <div class="field" style="left:134px;top:192px;width:217px;height:36px">Name</div>
  <div class="field" style="left:373px;top:192px;width:217px;height:36px">Email</div>
  <div class="field" style="left:610px;top:192px;width:217px;height:36px">Phone</div>
  <div class="field" style="left:849px;top:192px;width:217px;height:36px">Date
    <svg style="position:absolute;right:10px;top:11px" width="13" height="13" viewBox="0 0 13 13"><rect x="0.5" y="2" width="12" height="10.5" fill="#555"/><rect x="2" y="5" width="9" height="6" fill="#fff"/><rect x="3" y="0" width="2" height="3" fill="#555"/><rect x="8" y="0" width="2" height="3" fill="#555"/></svg>
  </div>
  <div class="field" style="left:134px;top:252px;width:932px;height:124px">Message</div>
  <div class="btn-light" style="left:545px;top:404px;width:110px;height:44px">BOOK NOW</div>
</section>

<footer class="footer">
  <div class="footer-links"><span>Home</span><span>About</span><span>Yachts</span><span>Services</span><span>Gallery</span><span>Contact Us</span><span>Book Now</span></div>
  <div class="copyright">Copyright © 2018 Brellavon. All rights reserved.</div>
  <div class="social"><span></span><span></span><span></span><span></span></div>
</footer>

</body>
</html>
```